Photography Studio Website (Design Only)

*Profile:
Omar Tenzali Studios is a boutique photography and art studio, and specialize in mixed media and digital arts. We offer a personalized and distinct portraiture photographic experience that does not only capture the natural magic of our clients' personality, but also spices it up with our own creative sauce to turn their images into timeless work of art that they can be proud to show off.
In addition to Portrait Photography, our studio also caters for art lovers who are passionate about decorating their space with unique pieces of art, we offer a huge collection of photographic and digitally painted artwork from our own art line collection.
Clients looking for the ultimate portraiture or fine art experience will be treated to a larger than life custom-designed artwork for them to share and enjoy for lifetime.
*What we need:
We need to design a cohesive website (Portfolio+Blog) that reflects the nature of our high-quality artwork and professional portrait photography service level specially in Glamour and Conceptual portraits. Also Since we also sell art prints in addition to portrait work we need the website to reflect that sense of high-end art gallery.
*The Design Aesthetics:
- Sophisticated
- Clean
- Artistic
- User Friendly (Easy/simple to navigate)
- The main focus of website is the images
*Content:
-Menu:
Home | Passion & Vision | Experiences | Portfolios | Connect | Testimonials | Blog | The Store
- Home Page:
Slideshow (with headlines)
Under the Slideshow we need to have 4 blocks that feature our main categories of specialty:
1-Glamour Portraits
2- Conceptual Portraits
3- Travel Art Photography
4- Fine Arts Photography
The blocks will show the latests blog posts in each respective category (5 lines under each block: post title only)- something similar to this: http://dravenholt.com
- Search box
- Social Media Icons: Facebook | Twitter | Pinterest| Instagram | YouTube
- Information & News Updates E-mail Subscription box
- Brand Colors: Attached PDF has the logo & Colors in Vector (Please stick to brand colors only)
- Brand Fonts:
JosefinSansStd-Light
You can check the current design on the following link:
Www.omartenzalistudios.com
Target Market(s)
Main Target: Women (25-40 yrs) | Secondary Targets: Artists & Musicians | Art Collectors
Industry/Entity Type
Portrait Photography
Look and feel

```html
<!DOCTYPE html>
<html lang="en">
<head>
<meta charset="utf-8">
<title>Omar Tenzali Studios</title>
<link rel="stylesheet" href="https://fonts.googleapis.com/css2?family=Josefin+Sans:wght@300;400;600&display=swap">
<style>
:root{
  --cream:#f4f0e7;
  --cream-deep:#ece5d6;
  --tan:#d6b77e;
  --tan-soft:#e7cf9f;
  --gold:#c9a55f;
  --ink:#2a2622;
  --text:#3b3630;
  --muted:#b9a98a;
  --line:#e2d9c6;
  --white:#ffffff;
}
*{box-sizing:border-box;margin:0;padding:0}
html,body{width:1200px;height:2262px;overflow:hidden}
body{
  position:relative;
  background:var(--cream);
  font-family:"Josefin Sans",sans-serif;
  font-weight:300;
  color:var(--text);
}
.header-band{
  position:absolute;left:0;top:0;width:1200px;height:692px;
  background:linear-gradient(180deg,#e6cf9e 0%,#ead6ab 55%,#efdfbd 100%);
}
.brand{
  position:absolute;left:484px;top:43px;width:232px;height:232px;border-radius:50%;
  background:var(--white);border:5px solid #f1e4c3;
  display:flex;flex-direction:column;align-items:center;justify-content:center;
  text-align:center;
}
.brand-mark{width:56px;height:56px;border:2px solid var(--gold);margin-bottom:16px}
.brand-name{font-size:21px;font-weight:400;color:var(--ink);line-height:1.15;letter-spacing:.5px}
.main-nav{
  position:absolute;left:220px;top:322px;display:flex;gap:0;align-items:center;
}
.main-nav a{
  display:block;height:32px;line-height:34px;padding:0 19px;
  font-size:14px;font-weight:400;color:var(--ink);text-decoration:none;text-transform:uppercase;
}
.main-nav a.is-active{background:#151310;color:var(--white);border-radius:4px;padding:0 20px;margin-right:9px}
.main-nav a+ a{margin-left:8px}
.hero{
  position:absolute;left:67px;top:421px;width:1066px;height:555px;
  border:6px solid var(--white);
  box-shadow:0 26px 26px -14px rgba(0,0,0,.55);
}
.hero-photo{width:100%;height:100%;background:radial-gradient(ellipse at 55% 45%,#c8a27d 0%,#8e7358 30%,#4d4b4b 70%,#3a3a3c 100%)}
.hero-arrow{
  position:absolute;top:243px;width:70px;height:70px;border-radius:50%;
  background:rgba(255,255,255,.42);display:flex;align-items:center;justify-content:center;
}
.hero-arrow.prev{left:6px}
.hero-arrow.next{right:6px}
.intro{
  position:absolute;left:65px;top:1080px;width:1070px;
  text-align:center;font-size:15px;line-height:24px;color:var(--tan);
}
.categories{position:absolute;left:65px;top:1232px;width:1070px;display:flex;gap:32px}
.category{width:244px}
.category h2{font-size:18px;font-weight:400;color:var(--ink);text-transform:uppercase;white-space:nowrap;margin-bottom:14px}
.category-photo{
  width:244px;height:163px;border:4px solid var(--white);outline:1px solid var(--line);
}
.category ul{list-style:none;margin-top:26px;padding-left:32px}
.category li{position:relative;font-size:13.5px;line-height:21px;color:var(--ink);font-weight:400}
.category li::before{
  content:"";position:absolute;left:-32px;top:6px;
  border-left:7px solid var(--tan);border-top:4px solid transparent;border-bottom:4px solid transparent;
}
.search{
  position:absolute;left:325px;top:1668px;width:444px;height:47px;border-radius:24px;
  background:#f6f3ec;border:1px solid var(--line);
  display:flex;align-items:center;justify-content:space-between;padding:0 22px 0 42px;
  font-size:16px;color:var(--muted);
}
.divider{position:absolute;left:65px;top:1806px;width:1070px;height:1px;background:var(--line)}
.news-title{position:absolute;left:65px;top:1888px;font-size:20px;font-weight:400;color:var(--ink)}
.news-item{position:absolute;left:65px;width:480px;display:flex;gap:34px}
.news-date{
  width:63px;flex:none;text-align:center;color:var(--ink);font-weight:400;
}
.news-date .day-month{background:var(--tan-soft);height:55px;padding-top:10px;font-size:14px;line-height:17px}
.news-date .year{font-size:13px;letter-spacing:5px;margin-top:4px;color:var(--gold)}
.news-item p{font-size:15px;line-height:23px;color:var(--tan);margin-top:-2px}
.newsletter{
  position:absolute;left:665px;top:1896px;width:466px;height:46px;
  background:var(--white);display:flex;align-items:center;justify-content:space-between;
  padding-left:22px;font-size:13px;color:var(--muted);
}
.newsletter button{
  width:172px;height:40px;margin-right:3px;border:0;background:var(--tan-soft);
  font-family:inherit;font-size:12px;font-weight:600;color:var(--ink);text-transform:uppercase;
}
.get-in-touch{position:absolute;left:767px;top:2006px;font-size:17px;font-weight:600;color:var(--tan-soft)}
.social{position:absolute;left:943px;top:1994px;display:flex;gap:4px}
.social span{width:35px;height:35px;border-radius:4px;background:var(--gold)}
.footer{
  position:absolute;left:332px;top:2168px;width:537px;height:39px;border-radius:20px;
  border:1px solid var(--line);background:#f6f3ec;
  display:flex;align-items:center;justify-content:center;gap:8px;
  font-size:14px;color:var(--muted);
}
.footer strong{font-weight:400;font-size:19px;color:var(--ink)}
</style>
</head>
<body>
  <div class="header-band" role="img" aria-label="Soft golden floral damask pattern"></div>

  <div class="brand">
    <div class="brand-mark"></div>
    <div class="brand-name">OMAR TENZALI<br>STUDIOS</div>
  </div>

  <nav class="main-nav">
    <a class="is-active" href="#">Home</a>
    <a href="#">Passion and Vision</a>
    <a href="#">Experience</a>
    <a href="#">Portfolio</a>
    <a href="#">Testimonials</a>
    <a href="#">Blog</a>
    <a href="#">Contact Us</a>
  </nav>

  <section class="hero">
    <div class="hero-photo" role="img" aria-label="Glamour portrait of a woman with windswept blonde hair"></div>
    <div class="hero-arrow prev"><svg width="22" height="28" viewBox="0 0 22 28"><path d="M16 3 5 14l11 11" fill="none" stroke="#fff" stroke-width="5"/></svg></div>
    <div class="hero-arrow next"><svg width="22" height="28" viewBox="0 0 22 28"><path d="M6 3l11 11L6 25" fill="none" stroke="#fff" stroke-width="5"/></svg></div>
  </section>

  <p class="intro">mbled it to make a type specimen book. It has survived not onlyorem Ipse printing and typesetting industry. Lorem Ipsum has been the industry's standard dummy text ever since the 1500s, when an unknown printer took a galley of type and scrambled it to make a type specimen book. It has survived not only</p>

  <section class="categories">
    <article class="category">
      <h2>Glamor Porttrait</h2>
      <div class="category-photo" role="img" aria-label="Glamour portrait photograph" style="background:linear-gradient(135deg,#f1e6d8,#d9b48a 55%,#b98a63)"></div>
      <ul><li>Blog Headline Goes Here</li><li>Blog Headline Goes Here</li><li>Blog Headline Goes Here</li><li>Blog Headline Goes Here</li><li>Blog Headline Goes Here</li></ul>
    </article>
    <article class="category">
      <h2>Conceptual Porttrait</h2>
      <div class="category-photo" role="img" aria-label="Conceptual still life with red paint on white" style="background:radial-gradient(circle at 40% 45%,#b8323a 0%,#d98a8c 18%,#f1eeee 40%,#e6e3e3 100%)"></div>
      <ul><li>Blog Headline Goes Here</li><li>Blog Headline Goes Here</li><li>Blog Headline Goes Here</li><li>Blog Headline Goes Here</li><li>Blog Headline Goes Here</li></ul>
    </article>
    <article class="category">
      <h2>Travel Art Photography</h2>
      <div class="category-photo" role="img" aria-label="Colourful harbour town waterfront" style="background:linear-gradient(180deg,#a9c7e6 0%,#d8a85c 40%,#c9714d 60%,#2f7fa8 100%)"></div>
      <ul><li>Blog Headline Goes Here</li><li>Blog Headline Goes Here</li><li>Blog Headline Goes Here</li><li>Blog Headline Goes Here</li><li>Blog Headline Goes Here</li></ul>
    </article>
    <article class="category">
      <h2>Fine Art Photography</h2>
      <div class="category-photo" role="img" aria-label="Black and white fine art portrait" style="background:radial-gradient(circle at 50% 50%,#8a8a8a 0%,#3a3a3a 45%,#111 100%)"></div>
      <ul><li>Blog Headline Goes Here</li><li>Blog Headline Goes Here</li><li>Blog Headline Goes Here</li><li>Blog Headline Goes Here</li><li>Blog Headline Goes Here</li></ul>
    </article>
  </section>

  <div class="search">
    <span>Search Keywords</span>
    <svg width="34" height="30" viewBox="0 0 34 30"><circle cx="15" cy="13" r="10" fill="none" stroke="#c9a55f" stroke-width="3.5"/><path d="M22 20l8 6" stroke="#c9a55f" stroke-width="4" stroke-linecap="round"/></svg>
  </div>

  <div class="divider"></div>

  <h3 class="news-title">LATES NEWS</h3>
  <div class="news-item" style="top:1938px">
    <div class="news-date"><div class="day-month">23<br>MAY</div><div class="year">2013</div></div>
    <p>mbled it to make a type specimen book. It has survived not onlyorem Ipse printing and typesetting industry. Lorem Ipsum has been the indus-</p>
  </div>
  <div class="news-item" style="top:2030px">
    <div class="news-date"><div class="day-month">23<br>MAY</div><div class="year">2013</div></div>
    <p>mbled it to make a type specimen book. It has survived not onlyorem Ipse printing and typesetting industry. Lorem Ipsum has been the indus-</p>
  </div>

  <form class="newsletter">
    <span>Enter Your Email Address Here</span>
    <button type="button">Sign up for Newsletter</button>
  </form>

  <div class="get-in-touch">GET IN TOUCH :</div>
  <div class="social"><span></span><span></span><span></span><span></span><span></span></div>

  <footer class="footer">All copyright are reserve by <strong>OMARTENZALISTUDIOS.COM</strong></footer>
</body>
</html>
```